Electrician Letterhead Design BLR

We need some letterhead for our bills and other papers.
Customer address is on the right side (Swiss format)
A4 format

Design should also be applicable on Cards

Target Market(s)

Private Customers, Small Business

Industry/Entity Type

Electrician

Other font styles liked:
• incised 901

Colors
00AB8E
00BBA5
67D7C9
C6EFE9
E9F9F6

```html
<!DOCTYPE html>
<html lang="de">
<head>
<meta charset="utf-8">
<title>BLR Letterhead</title>
<link href="https://fonts.googleapis.com/css2?family=Poppins:wght@400;700&display=swap" rel="stylesheet">
<style>
  :root {
    --teal: #009d8c;
    --teal-light: #67d7c9;
    --ink: #000000;
    --text: #111111;
    --rule: #ececec;
    --paper: #ffffff;
  }
  html, body {
    margin: 0;
    padding: 0;
    overflow: hidden;
    background: var(--paper);
  }
  .letterhead {
    position: relative;
    width: 849px;
    height: 1200px;
    background: var(--paper);
    overflow: hidden;
    font-family: "Poppins", sans-serif;
  }
  .brand {
    position: absolute;
    left: 40px;
    top: 52px;
    display: flex;
    align-items: center;
    gap: 14px;
  }
  .brand-square {
    width: 22px;
    height: 22px;
    background: var(--teal);
  }
  .brand-name {
    font-weight: 700;
    font-size: 80px;
    line-height: 1;
    color: var(--teal);
    letter-spacing: 2px;
  }
  .contact {
    position: absolute;
    right: 36px;
    top: 40px;
    margin: 0;
    padding: 0;
    list-style: none;
  }
  .contact li {
    display: flex;
    align-items: center;
    justify-content: flex-end;
    height: 26.3px;
    font-size: 16.5px;
    color: var(--text);
  }
  .contact .icon {
    width: 15px;
    height: 15px;
    margin-left: 18px;
    fill: var(--teal);
  }
  .header-rule {
    position: absolute;
    left: 27px;
    right: 27px;
    top: 182px;
    height: 2px;
    background: linear-gradient(90deg, transparent, var(--rule) 8%, var(--rule) 92%, transparent);
  }
  .footer-bands {
    position: absolute;
    left: 0;
    bottom: 0;
    width: 849px;
    height: 140px;
  }
</style>
</head>
<body>
<div class="letterhead">
  <div class="brand">
    <span class="brand-name">BLR</span>
    <span class="brand-square"></span>
  </div>

  <ul class="contact">
    <li>Phone goes here
      <svg class="icon" viewBox="0 0 24 24"><path d="M6.6 10.8a15.1 15.1 0 0 0 6.6 6.6l2.2-2.2c.3-.3.7-.4 1-.2 1.1.4 2.3.6 3.6.6.6 0 1 .4 1 1V20c0 .6-.4 1-1 1A17 17 0 0 1 3 4c0-.6.4-1 1-1h3.5c.6 0 1 .4 1 1 0 1.3.2 2.5.6 3.6.1.3 0 .7-.2 1z"/></svg>
    </li>
    <li>Email goes here
      <svg class="icon" viewBox="0 0 24 24"><path d="M2 5h20v14H2z M4 7v.4l8 5.6 8-5.6V7z M4 9.8V17h16V9.8l-8 5.6z" fill-rule="evenodd"/></svg>
    </li>
    <li>Website goes here
      <svg class="icon" viewBox="0 0 24 24"><path d="M6 2l13 11h-6.5l3.5 7.5-3 1.4-3.5-7.6L6 19z"/></svg>
    </li>
    <li>Adress goes here
      <svg class="icon" viewBox="0 0 24 24"><path d="M12 2a7 7 0 0 0-7 7c0 5 7 13 7 13s7-8 7-13a7 7 0 0 0-7-7zm0 9.5A2.5 2.5 0 1 1 12 6.5a2.5 2.5 0 0 1 0 5z"/></svg>
    </li>
  </ul>

  <div class="header-rule"></div>

  <svg class="footer-bands" viewBox="0 0 849 140" preserveAspectRatio="none" aria-hidden="true">
    <polygon fill="var(--teal-light)" points="0,120 849,40 849,60 0,140"/>
    <polygon fill="var(--ink)" points="0,128 849,64 849,78 0,140"/>
    <polygon fill="var(--teal)" points="260,140 849,86 849,140"/>
  </svg>
</div>
</body>
</html>
```